Women's Health Company needs business card

We need a business card for a USA based women's health care company. We use digital technology to enhance therapy prescribed by clinicians for their patients

```html
<!DOCTYPE html>
<html lang="en">
<head>
<meta charset="utf-8">
<title>Novira Health — Business Card</title>
<link href="https://fonts.googleapis.com/css2?family=Open+Sans:wght@400;700&display=swap" rel="stylesheet">
<style>
  :root {
    --backdrop: #4a4a4a;
    --card-black: #141414;
    --teal: #7cc4c0;
    --purple: #8e55a0;
    --purple-light: #a46bb6;
    --white: #f4f4f4;
  }
  * { box-sizing: border-box; margin: 0; padding: 0; }
  html, body {
    width: 1200px; height: 801px; overflow: hidden;
    background: var(--backdrop);
    font-family: "Open Sans", Arial, sans-serif;
  }
  .stage {
    width: 1200px; height: 801px;
    display: flex; align-items: center; justify-content: center; gap: 40px;
  }
  .card {
    width: 540px; height: 309px;
    border-bottom: 4px solid var(--teal);
    border-right: 4px solid var(--teal);
    position: relative;
    box-shadow: 0 14px 30px rgba(0,0,0,.35);
  }
  .card--front { background: var(--card-black); display: flex; }
  .card--back { background: var(--purple); display: flex; align-items: center; justify-content: center; }

  .brand { display: flex; align-items: center; gap: 10px; }
  .brand__dot { width: 10px; height: 10px; border-radius: 50%; background: var(--purple); }
  .brand__name { font-weight: 700; color: var(--teal); font-size: 34px; letter-spacing: .5px; }

  .card--back .brand__dot { width: 14px; height: 14px; background: var(--purple-light); }
  .card--back .brand__name { color: var(--purple-light); font-size: 52px; }

  .front__logo { width: 290px; display: flex; align-items: center; justify-content: center; }
  .front__divider { width: 1.5px; background: var(--teal); margin: 40px 0; }
  .front__details { flex: 1; padding: 44px 0 0 26px; color: var(--white); }

  .person__name { color: var(--teal); font-weight: 700; font-size: 17px; text-transform: uppercase; letter-spacing: .3px; }
  .person__title { font-size: 13px; margin-top: 2px; }

  .contacts { list-style: none; margin-top: 18px; }
  .contacts li { display: flex; align-items: center; gap: 8px; font-size: 13px; line-height: 21px; }
  .contacts svg { width: 11px; height: 11px; fill: var(--teal); flex: none; }

  .address { font-size: 13px; line-height: 20px; margin-top: 16px; font-style: normal; }
</style>
</head>
<body>
<main class="stage">
  <section class="card card--front">
    <div class="front__logo">
      <div class="brand"><span class="brand__dot"></span><span class="brand__name">Novira Health</span></div>
    </div>
    <div class="front__divider"></div>
    <div class="front__details">
      <p class="person__name">Leah Marlowe</p>
      <p class="person__title">President</p>
      <ul class="contacts">
        <li><svg viewBox="0 0 24 24"><path d="M6.6 10.8a15.1 15.1 0 0 0 6.6 6.6l2.2-2.2c.3-.3.7-.4 1-.2 1.1.4 2.3.6 3.6.6.6 0 1 .4 1 1V20c0 .6-.4 1-1 1A17 17 0 0 1 3 4c0-.6.4-1 1-1h3.5c.6 0 1 .4 1 1 0 1.3.2 2.5.6 3.6.1.3 0 .7-.2 1z"/></svg>555 014 2286</li>
        <li><svg viewBox="0 0 24 24"><path d="M2 5h20v14H2z M2 5l10 8 10-8" /></svg>hello@novirahealth.com</li>
        <li><svg viewBox="0 0 24 24"><circle cx="12" cy="12" r="10"/></svg>www.novirahealth.com</li>
      </ul>
      <address class="address">4217 Cedar Cove Lane<br>Brightwater CA 92010</address>
    </div>
  </section>

  <section class="card card--back">
    <div class="brand"><span class="brand__dot"></span><span class="brand__name">Novira Health</span></div>
  </section>
</main>
</body>
</html>
```